Stationary Design for Norvath Digital

We are after a full stationary back business cards, letterheads, compliment slip, invoice template, delivery note and anything else we could use within the stationary pack.

We would also like an email footer creating.

Our company details to be included on all stationary:

Registered Name: Norvath Limited
Company Registration Number: 20473915
Website: www.norvathdigital.example
email: info@norvathdigital.example
Phone: 01632 960 417
Address: 48 Tamsin Lane Loughborough Leicestershire United Kingdom LE11 9QX

```html
<!DOCTYPE html>
<html lang="en">
<head>
<meta charset="utf-8">
<title>Norvath Digital Stationery</title>
<link href="https://fonts.googleapis.com/css2?family=Questrial&family=Arimo:wght@400;700&display=swap" rel="stylesheet">
<style>
:root{
  --navy:#0a3470;
  --slate:#7d8393;
  --ink:#222;
  --muted:#6b7080;
  --paper:#fff;
  --stage:#e2e2e4;
  --cell:#e7e8ea;
}
*{box-sizing:border-box;margin:0;padding:0}
html,body{width:1189px;height:1200px;overflow:hidden;background:var(--stage)}
body{position:relative;font-family:"Questrial",sans-serif;color:var(--ink)}
.piece{position:absolute;background:var(--paper);overflow:hidden}
.brand{font-family:"Questrial",sans-serif;color:var(--navy);letter-spacing:1px;line-height:1;position:absolute;white-space:nowrap}
.brand.light{color:#fff}
.band{position:absolute;left:0;right:0}
.navy{background:var(--navy)}
.slate{background:var(--slate)}
.tiny{font-size:5px}
.caption{color:#fff;text-align:center;position:absolute;left:0;right:0;white-space:nowrap}
.company{font-family:"Questrial",sans-serif;color:var(--navy);letter-spacing:1.5px;text-transform:uppercase;white-space:nowrap}
.contact{color:var(--muted);text-align:right;line-height:1.35;white-space:nowrap}
.reg{color:var(--navy)}
.body-copy{font-family:"Arimo",sans-serif;font-size:6.4px;line-height:10.6px;color:#222}
.body-copy p{margin-bottom:10.6px}
.signature{width:90px;height:22px;background:linear-gradient(90deg,#dcdfe6,#eef0f4);border-radius:2px}
table.items{border-collapse:collapse;width:100%;font-size:6.5px}
table.items th{background:var(--navy);color:#fff;font-weight:400;text-align:left;padding:4px 6px;height:17px}
table.items td{background:var(--cell);border:1px solid #fff;height:24px}
</style>
</head>
<body>

<!-- Presentation folder -->
<section class="piece folder" style="left:68px;top:94px;width:361px;height:467px">
  <div class="brand" style="left:120px;top:95px;font-size:30px">Norvath</div>
  <div class="band navy" style="top:165px;height:246px"></div>
  <div class="band slate" style="top:411px;height:56px"></div>
  <div class="caption tiny" style="top:436px">www.norvathdigital.example</div>
</section>

<!-- Letterhead -->
<section class="piece letterhead" style="left:476px;top:95px;width:361px;height:466px">
  <div class="brand" style="left:29px;top:50px;font-size:30px">Norvath</div>
  <div style="position:absolute;right:35px;top:32px;width:200px">
    <div class="company" style="font-size:9px;text-align:right;margin-bottom:6px">Norvath Limited</div>
    <div class="contact tiny">48 Tamsin Lane Brackwell<br>Hartshire United Kingdom BW4 9QX</div>
    <div class="contact tiny" style="margin-top:5px">01632 960 417 &#9632;<br>www.norvathdigital.example &#9632;</div>
    <div class="contact tiny reg" style="margin-top:2px">Company Registration Number: 20473915</div>
  </div>
  <div class="body-copy" style="position:absolute;left:28px;top:132px;line-height:1.3">
    <div style="font-weight:700;font-size:7px">ALDER QUINN</div>
    <div>Street Name, City Name.<br>Zip Coad 0000</div>
  </div>
  <div class="body-copy" style="position:absolute;left:28px;top:184px;width:306px">
    <p>Lorem Ipsum is simply dummy text of the printing and typesetting industry. Lorem Ipsum has been the industry's standard dummy text ever since the 1500s, when an unknown printer took a galley of type and scrambled it to make a type specimen book. It has survived not only five centuries, but also the leap into electronic typesetting, remaining essentially unchanged. It was popularised in the 1960s with the release of Letraset sheets containing Lorem Ipsum passages, and more recently with desktop publishing software like Aldus PageMaker including versions of Lorem Ipsum.</p>
    <p>It is a long established fact that a reader will be distracted by the readable content of a page when looking at its layout. The point of using Lorem Ipsum is that it has a more-or-less normal distribution of letters, as opposed to using 'Content here, content here', making it look like readable English. Many desktop publishing packages and web page editors now use Lorem Ipsum as their default model text, and a search for 'lorem ipsum' will uncover many web sites still in their infancy. Various versions have evolved over the years, sometimes by accident, sometimes on purpose (injected humour and the like).</p>
  </div>
  <div class="body-copy" style="position:absolute;left:28px;top:352px;line-height:1.2">
    <div>Regards,</div>
    <div class="signature" role="img" aria-label="Handwritten signature of Marta Lisle" style="margin:6px 0 4px"></div>
    <div style="font-weight:700">Marta Lisle</div>
    <div>General Manager</div>
  </div>
  <div class="band navy" style="top:434px;height:23px"></div>
  <div class="band slate" style="top:457px;height:9px"></div>
  <div class="caption tiny" style="top:443px">info@norvathdigital.example</div>
</section>

<!-- Invoice -->
<section class="piece invoice" style="left:879px;top:204px;width:250px;height:357px">
  <div class="brand" style="left:16px;top:32px;font-size:23px">Norvath</div>
  <div style="position:absolute;right:15px;top:14px;width:130px">
    <div class="company" style="font-size:8px;text-align:right;margin-bottom:3px">Norvath Limited</div>
    <div class="contact tiny">01632 960 417 &#9632;<br>info@norvathdigital.example &#9632;<br>www.norvathdigital.example &#9632;</div>
  </div>
  <div style="position:absolute;left:127px;top:59px;width:107px;height:20px;background:var(--navy);color:#fff;font-size:10px;font-weight:700;font-family:Arimo,sans-serif;text-align:center;line-height:20px;letter-spacing:.5px">INVOICE</div>
  <div style="position:absolute;left:127px;top:80px;width:107px;height:16px;background:var(--cell);display:flex;font-size:2.6px;color:var(--muted)">
    <span style="flex:1;padding:3px">TOTAL DUE</span><span style="flex:1;padding:3px">INVOICE DATE</span><span style="flex:1;padding:3px">INVOICE NO</span>
  </div>
  <div style="position:absolute;left:15px;top:126px;width:219px">
    <table class="items">
      <tr><th>Item Description</th><th>Unit Price</th><th>Quantity</th><th>Total</th></tr>
      <tr><td></td><td></td><td></td><td></td></tr>
      <tr><td></td><td></td><td></td><td></td></tr>
      <tr><td></td><td></td><td></td><td></td></tr>
      <tr><td></td><td></td><td></td><td></td></tr>
      <tr><td></td><td></td><td></td><td></td></tr>
      <tr><td></td><td></td><td></td><td></td></tr>
    </table>
  </div>
  <div style="position:absolute;left:164px;top:288px;width:70px;height:20px;background:var(--navy);color:#fff;font-size:4.5px;padding:4px 8px;line-height:1.6">SUB TEXT :<br>TAX VAT :</div>
  <div style="position:absolute;left:164px;top:309px;width:70px;height:10px;background:var(--cell);color:var(--navy);font-size:4.5px;padding:2px 8px">TOTAL :</div>
  <div class="tiny reg" style="position:absolute;left:15px;top:323px">Company Registration Number: 20473915</div>
  <div style="position:absolute;left:15px;top:331px;width:219px;height:1px;background:var(--navy)"></div>
  <div class="tiny" style="position:absolute;left:0;right:0;top:338px;text-align:center;color:var(--muted)">48 Tamsin Lane Brackwell Hartshire United Kingdom BW4 9QX</div>
</section>

<!-- Compliment slip -->
<section class="piece slip" style="left:68px;top:657px;width:364px;height:182px">
  <div class="brand" style="left:16px;top:26px;font-size:22px">Norvath</div>
  <div class="band navy" style="top:158px;height:15px"></div>
  <div class="band slate" style="top:173px;height:9px"></div>
  <div class="caption tiny" style="top:163px">48 Tamsin Lane Brackwell Hartshire United Kingdom BW4 9QX</div>
</section>

<!-- Memory stick labels -->
<section class="piece tag-light" style="left:476px;top:634px;width:130px;height:51px">
  <div class="brand" style="left:30px;top:19px;font-size:14px">Norvath</div>
  <div style="position:absolute;right:0;top:0;width:24px;height:51px;background:#222"></div>
</section>
<section class="piece tag-dark" style="left:641px;top:634px;width:130px;height:51px;background:var(--navy)">
  <div class="brand light" style="left:24px;top:19px;font-size:14px">Norvath</div>
  <div style="position:absolute;right:0;top:0;width:24px;height:51px;background:#f2f2f2"></div>
</section>

<!-- Notebook -->
<section class="piece notebook" style="left:889px;top:609px;width:200px;height:277px">
  <div class="brand" style="left:65px;top:42px;font-size:17px">Norvath</div>
  <div class="band" style="top:90px;height:158px;background:#1f3a6e"></div>
  <div class="band slate" style="top:248px;height:29px"></div>
  <div class="caption" style="top:259px;font-size:3px">www.norvathdigital.example</div>
</section>

<!-- Envelope -->
<section class="piece envelope" style="left:68px;top:898px;width:364px;height:183px">
  <div style="position:absolute;left:0;top:0;width:364px;height:51px;background:var(--navy);clip-path:polygon(0 0,100% 0,98% 100%,2% 100%)"></div>
  <div class="brand light" style="left:152px;top:18px;font-size:16px">Norvath</div>
</section>

<!-- Business card front -->
<section class="piece card-front" style="left:478px;top:747px;width:271px;height:153px;background:var(--navy)">
  <div class="brand light" style="left:80px;top:60px;font-size:30px">Norvath</div>
  <div class="band slate" style="top:139px;height:14px"></div>
  <div class="caption" style="top:141px;font-size:7px">www.norvathdigital.example</div>
</section>

<!-- Business card back -->
<section class="piece card-back" style="left:478px;top:927px;width:270px;height:153px">
  <div class="brand" style="left:15px;top:36px;font-size:27px">Norvath</div>
  <div style="position:absolute;right:13px;top:28px;text-align:right">
    <div class="company" style="font-size:9px">Alder Quinn</div>
    <div style="font-size:7px;color:var(--muted)">President</div>
  </div>
  <div class="band navy" style="top:92px;height:46px"></div>
  <div style="position:absolute;left:14px;top:98px;color:#fff;font-size:7px;line-height:1.35;white-space:nowrap">&#9742; 01632 960 417<br>&#9632; www.norvathdigital.example<br><span style="font-size:4.5px">Company Registration Number: 20473915</span></div>
  <div style="position:absolute;right:13px;top:98px;color:#fff;font-size:7px;line-height:1.35;text-align:right;white-space:nowrap">48 Tamsin Lane Brackwell<br>Hartshire<br>United Kingdom BW4 9QX</div>
  <div class="band slate" style="top:138px;height:15px"></div>
  <div class="caption" style="top:141px;font-size:7px">info@norvathdigital.example</div>
</section>

<!-- Wide business card -->
<section class="piece card-wide" style="left:783px;top:916px;width:346px;height:163px">
  <div class="brand" style="left:12px;top:62px;font-size:21px">Norvath</div>
  <div style="position:absolute;left:107px;top:46px;width:1px;height:56px;background:var(--navy)"></div>
  <div style="position:absolute;left:120px;top:55px">
    <div class="company" style="font-size:9px;margin-bottom:6px">Norvath Limited</div>
    <div style="font-size:7px;color:var(--muted);line-height:1.3;white-space:nowrap">&#9632; 01632 960 417<br>&#9632; info@norvathdigital.example<br>&#9632; www.norvathdigital.example</div>
  </div>
  <div style="position:absolute;left:223px;top:46px;width:1px;height:56px;background:var(--navy)"></div>
  <div style="position:absolute;left:235px;top:72px;font-size:7px;color:var(--muted);line-height:1.3;white-space:nowrap">48 Tamsin Lane<br>Brackwell Hartshire<br>United Kingdom BW4 9QX</div>
  <div class="band navy" style="top:142px;height:14px"></div>
  <div class="band slate" style="top:156px;height:7px"></div>
  <div class="caption" style="top:144px;font-size:7px">Company Registration Number: 20473915</div>
</section>

</body>
</html>
```